Maple Ridge business card design

Card needs to include the following text/items:
Company Logo
Tobin Marsh
Phone # - 555-318-7642
service@mapleridgelandscaping.example
Lawn & landscape maintenance services

```html
<!DOCTYPE html>
<html lang="en">
<head>
<meta charset="utf-8">
<title>Maple Ridge Business Card</title>
<link rel="stylesheet" href="https://fonts.googleapis.com/css2?family=Cinzel:wght@400;600;700&family=Montserrat:wght@400;500&display=swap">
<style>
  :root {
    --page-bg: #2b2b2b;
    --card-top: #333333;
    --card-bottom: #1c1c1c;
    --text-light: #f2f2f2;
    --accent-gold: #e0a81c;
    --accent-green: #8a9a2e;
    --rule-green: #6f7d2a;
  }
  * { box-sizing: border-box; margin: 0; padding: 0; }
  html, body { width: 1200px; height: 900px; overflow: hidden; }
  body {
    background: var(--page-bg);
    display: flex;
    align-items: center;
    justify-content: center;
    gap: 90px;
  }
  .card {
    position: relative;
    width: 340px;
    height: 600px;
    border-radius: 26px;
    background: linear-gradient(160deg, var(--card-top) 0%, var(--card-bottom) 100%);
    box-shadow: 0 18px 40px rgba(0,0,0,0.45);
    color: var(--text-light);
    overflow: hidden;
  }
  .brand {
    position: absolute;
    top: 110px;
    left: 0;
    right: 0;
    display: flex;
    flex-direction: column;
    align-items: center;
  }
  .brand-dot {
    width: 22px;
    height: 22px;
    border-radius: 50%;
    background: var(--accent-gold);
    margin-bottom: 16px;
  }
  .brand-name {
    font-family: "Cinzel", serif;
    font-weight: 700;
    font-size: 34px;
    letter-spacing: 1px;
    line-height: 1;
    color: var(--text-light);
  }
  .brand-sub {
    font-family: "Cinzel", serif;
    font-weight: 400;
    font-size: 12px;
    letter-spacing: 10px;
    margin-top: 6px;
    margin-right: -10px;
    color: var(--accent-gold);
  }
  .card--back .brand { top: 70px; }
  .tagline {
    position: absolute;
    bottom: 56px;
    left: 0;
    right: 0;
    text-align: center;
    font-family: "Cinzel", serif;
    font-weight: 600;
    font-size: 19px;
    line-height: 1.45;
    letter-spacing: 1.5px;
  }
  .contact-block {
    position: absolute;
    left: 30px;
    right: 22px;
    bottom: 80px;
  }
  .person-name {
    font-family: "Cinzel", serif;
    font-weight: 700;
    font-size: 26px;
    color: var(--accent-green);
  }
  .person-name .surname { color: var(--accent-gold); }
  .person-role {
    font-family: "Montserrat", sans-serif;
    font-weight: 500;
    font-size: 15px;
    margin-top: 2px;
  }
  .rule {
    height: 1px;
    background: var(--rule-green);
    margin: 18px 0 16px 40px;
  }
  .contact-icons { display: flex; gap: 6px; }
  .contact-icons svg { width: 18px; height: 18px; }
  .contact-lines {
    font-family: "Montserrat", sans-serif;
    font-size: 11.5px;
    line-height: 1.9;
    padding: 6px 0 0 24px;
    white-space: nowrap;
  }
</style>
</head>
<body>
  <section class="card card--front">
    <div class="brand">
      <span class="brand-dot"></span>
      <span class="brand-name">Maple Ridge</span>
      <span class="brand-sub">Landscaping</span>
    </div>
    <p class="tagline">Lawn &amp; Landscape<br>Maintenance Services</p>
  </section>

  <section class="card card--back">
    <div class="brand">
      <span class="brand-dot"></span>
      <span class="brand-name">Maple Ridge</span>
      <span class="brand-sub">Landscaping</span>
    </div>
    <div class="contact-block">
      <h1 class="person-name">Tobin <span class="surname">Marsh</span></h1>
      <p class="person-role">Managing Director</p>
      <div class="rule"></div>
      <div class="contact-icons">
        <svg viewBox="0 0 20 20" aria-hidden="true">
          <circle cx="10" cy="10" r="10" fill="#e0a81c"/>
          <path d="M6.5 5.5l2 0 1 2.5-1.3 1a6 6 0 0 0 2.8 2.8l1-1.3 2.5 1v2a1 1 0 0 1-1 1A8 8 0 0 1 5.5 6.5a1 1 0 0 1 1-1z" fill="#1c1c1c"/>
        </svg>
        <svg viewBox="0 0 20 20" aria-hidden="true">
          <circle cx="10" cy="10" r="10" fill="#e0a81c"/>
          <rect x="5" y="6.5" width="10" height="7" rx="1" fill="none" stroke="#1c1c1c" stroke-width="1.3"/>
          <path d="M5.5 7l4.5 3.5L14.5 7" fill="none" stroke="#1c1c1c" stroke-width="1.3"/>
        </svg>
      </div>
      <div class="contact-lines">
        <p>555-318-7642</p>
        <p>service@mapleridgelandscaping.example</p>
      </div>
    </div>
  </section>
</body>
</html>
```